" A empresa atua em dois segmentos: 1) atendimento psicológico de crianças, adolescentes e adultos e 2) recrutamento, seleçao e treinamento de pessoas. A proposta é trabalhar com o desenvolvimento humano em suas diversas dimensoes. "

```html
<!DOCTYPE html>
<html lang="pt-BR">
<head>
<meta charset="UTF-8">
<title>Nova Trilha – Placa de Fachada</title>
<link href="https://fonts.googleapis.com/css2?family=Questrial&display=swap" rel="stylesheet">
<style>
  :root {
    --backdrop: #a8693d;
    --sign-white: #ffffff;
    --brand-teal: #2a9d9a;
    --deep-teal: #1f7f7c;
    --text-grey: #555a5c;
    --faint-grey: #dcdcdc;
  }
  * { margin: 0; padding: 0; box-sizing: border-box; }
  html, body {
    width: 1200px;
    height: 1200px;
    overflow: hidden;
    background: var(--backdrop);
    font-family: "Questrial", "Century Gothic", sans-serif;
  }
  .sign {
    position: absolute;
    left: 100px;
    top: 595px;
    width: 1000px;
    height: 155px;
  }
  .sign-shape {
    position: absolute;
    inset: 0;
    filter: drop-shadow(0 6px 10px rgba(0,0,0,0.25));
  }
  .brand-dot {
    position: absolute;
    left: 30px;
    top: 20px;
    width: 76px;
    height: 76px;
    border-radius: 50%;
    background: var(--brand-teal);
  }
  .brand-name {
    position: absolute;
    left: 164px;
    top: 14px;
    font-size: 62px;
    line-height: 1;
    color: var(--brand-teal);
    white-space: nowrap;
  }
  .brand-tagline {
    position: absolute;
    left: 166px;
    top: 92px;
    font-size: 22px;
    letter-spacing: 1.5px;
    color: var(--text-grey);
    white-space: nowrap;
  }
  .contact {
    position: absolute;
    left: 505px;
    top: 14px;
    width: 460px;
    text-align: center;
    white-space: nowrap;
  }
  .contact-line { display: block; line-height: 1.22; }
  .contact-address { font-size: 27px; color: var(--brand-teal); letter-spacing: 1px; }
  .contact-phone { font-size: 24px; color: var(--deep-teal); letter-spacing: 0.5px; }
  .contact-web { font-size: 23px; color: var(--text-grey); text-align: right; padding-right: 8px; }
</style>
</head>
<body>
  <div class="sign">
    <svg class="sign-shape" width="1000" height="155" viewBox="0 0 1000 155" aria-hidden="true">
      <defs>
        <clipPath id="sign-outline">
          <path d="M0 155 V45 Q0 0 45 0 H1000 V155 Z"/>
        </clipPath>
      </defs>
      <path d="M0 155 V45 Q0 0 45 0 H1000 V155 Z" fill="var(--sign-white)"/>
      <circle cx="932" cy="72" r="82" fill="var(--faint-grey)" clip-path="url(#sign-outline)"/>
    </svg>

    <span class="brand-dot" aria-hidden="true"></span>
    <div class="brand-name">Nova Trilha</div>
    <div class="brand-tagline">Desenvolvimento Humano</div>

    <address class="contact" style="font-style: normal;">
      <span class="contact-line contact-address">Av. Aurora n°410</span>
      <span class="contact-line contact-address">Campo Verde&nbsp; S.P.</span>
      <span class="contact-line contact-phone">11 5555-0123/11 5555-0456</span>
      <span class="contact-line contact-web">www.novatrilha.com.br</span>
    </address>
  </div>
</body>
</html>
```